Business Card Design

I have two logos , one is for the front of the card and the other for the back. The front image is the road and the sun, the back image should be the atom with the motto at the bottom. The back of the card should be black with the atom and lettering white. The front should have the image with the road and lettering black with the yellow sun all on a white background.
Updates

I have changed what I would like done. The only logo I want to use is the atom logo. White lettering with a black background on the front and back of the card. There should be no contact info on the back of the card. On the back there should b the logo with company name and the slogan underneath at the bottom of the card, also on the back if you can have the logo  image in the background as well in a gray or silver can be tiled or cascade of some sort.

On the front it should have all of the contact info with an email address added  tidewaveprints@fernmail.net   Black background with white lettering and another larger image of the logo in a gray or silver in the background. The logo and name side by side with the slogan directly under the name.

Industry/Entity Type

Business

Contact Information for Business Card

Colin Marsh
Director of Operations
6182 Hollis Ln #517
Georgetown, TX 78415
Cell: (512)487-3056
Fax: (512)871-4402

```html
<!DOCTYPE html>
<html lang="en">
<head>
<meta charset="UTF-8">
<title>Lonestar Portable Imaging – Business Card</title>
<link href="https://fonts.googleapis.com/css2?family=Quicksand:wght@400;500&display=swap" rel="stylesheet">
<style>
  :root {
    --page: #e9e9e9;
    --card: #0b0b0b;
    --ink: #ffffff;
    --ink-soft: #cfcfcf;
    --silver-deep: #141414;
    --silver-dark: #262626;
    --silver-mid: #3d3d3d;
    --silver-light: #4a4a4a;
    --shadow: rgba(0, 0, 0, 0.28);
  }
  * { box-sizing: border-box; margin: 0; padding: 0; }
  html, body {
    width: 1200px;
    height: 849px;
    overflow: hidden;
    background: var(--page);
    font-family: "Quicksand", sans-serif;
    color: var(--ink);
  }
  .sheet {
    position: relative;
    width: 1200px;
    height: 849px;
    display: flex;
    align-items: center;
    justify-content: center;
    gap: 60px;
  }
  .card {
    position: relative;
    width: 520px;
    height: 297px;
    background: var(--card);
    overflow: hidden;
    box-shadow: 0 14px 30px var(--shadow);
  }

  /* Back side: area reserved for the tiled grey mark pattern */
  .tiled-mark {
    position: absolute;
    inset: 0;
    background:
      radial-gradient(ellipse 60% 55% at 22% 30%, var(--silver-light) 0%, transparent 70%),
      radial-gradient(ellipse 55% 60% at 78% 25%, var(--silver-mid) 0%, transparent 70%),
      radial-gradient(ellipse 60% 55% at 70% 80%, var(--silver-light) 0%, transparent 70%),
      radial-gradient(ellipse 50% 50% at 25% 85%, var(--silver-mid) 0%, transparent 70%),
      linear-gradient(135deg, var(--silver-dark) 0%, var(--silver-deep) 50%, var(--silver-dark) 100%);
  }
  .back .brand {
    position: absolute;
    left: 40px;
    top: 100px;
  }

  /* Brand lockup */
  .brand {
    display: flex;
    align-items: center;
    gap: 14px;
  }
  .brand-dot {
    flex: none;
    width: 40px;
    height: 40px;
    border-radius: 50%;
    border: 3px solid var(--ink);
  }
  .brand-name {
    font-weight: 500;
    font-size: 28px;
    line-height: 1.1;
    letter-spacing: 0.2px;
    white-space: nowrap;
  }
  .brand-slogan {
    font-weight: 400;
    font-size: 15px;
    color: var(--ink-soft);
    margin-top: 5px;
    letter-spacing: 0.3px;
  }

  /* Front side */
  .large-mark {
    position: absolute;
    right: -50px;
    bottom: -70px;
    width: 360px;
    height: 260px;
    border-radius: 50%;
    background: radial-gradient(ellipse at center, var(--silver-light) 0%, var(--silver-dark) 50%, transparent 72%);
  }
  .front .brand {
    position: absolute;
    left: 30px;
    top: 24px;
    gap: 10px;
  }
  .front .brand-dot { width: 26px; height: 26px; border-width: 2px; }
  .front .brand-name { font-size: 17px; }
  .front .brand-slogan { font-size: 10px; margin-top: 2px; }

  .person {
    position: absolute;
    left: 0;
    right: 0;
    top: 94px;
    text-align: center;
  }
  .person-name {
    font-weight: 500;
    font-size: 18px;
    letter-spacing: 0.6px;
    text-transform: uppercase;
  }
  .person-title {
    font-size: 12px;
    color: var(--ink-soft);
    margin-top: 3px;
  }
  .contact {
    position: absolute;
    left: 30px;
    top: 168px;
    font-size: 13px;
    line-height: 1.6;
    font-style: normal;
  }
</style>
</head>
<body>
  <main class="sheet">
    <section class="card back" aria-label="Card back">
      <div class="tiled-mark" role="img" aria-label="Tiled grey pattern of the company mark repeated across the whole card"></div>
      <div class="brand">
        <span class="brand-dot"></span>
        <div>
          <p class="brand-name">Lonestar Portable Imaging</p>
          <p class="brand-slogan">Professional Timely Accurate</p>
        </div>
      </div>
    </section>

    <section class="card front" aria-label="Card front">
      <div class="large-mark" role="img" aria-label="Large faint grey company mark in the background"></div>
      <div class="brand">
        <span class="brand-dot"></span>
        <div>
          <p class="brand-name">Lonestar Portable Imaging</p>
          <p class="brand-slogan">Professional Timely Accurate</p>
        </div>
      </div>
      <div class="person">
        <p class="person-name">Colin Marsh</p>
        <p class="person-title">Director of Operations</p>
      </div>
      <address class="contact">
        <p>6182 Hollis Ln #517 Georgetown, TX 78415</p>
        <p>Cell: (512)487-3056 Fax: (512)871-4402</p>
        <p>tidewaveprints@fernmail.net</p>
      </address>
    </section>
  </main>
</body>
</html>
```